FernMill Coatings website development for protective coatings manufacturer

We require a website for a new company which manufacturers protective coatings for automotive and industrial applications. We have a new logo which can be used and will be uploaded for inclusion on the website. There should be the following pages:
Home
About us
Products
Distribution
Contact us
There will be 10 products with downloadable pdf files TDS and MSDS.
Target Market(s)
Automotive and industrial coatings
Industry/Entity Type
Protective Coatings manufacturing
Coding
Coded - Design and coding required
Font styles to use
Sans Serif
Requirements
Must have
- Nice and clear images related to the target market

```html
<!DOCTYPE html>
<html lang="en">
<head>
<meta charset="utf-8">
<title>FernMill Coatings</title>
<link rel="stylesheet" href="https://fonts.googleapis.com/css2?family=Montserrat:wght@400;500;600;700;800&display=swap">
<style>
:root{
  --blue:#2b5a92;
  --blue-dark:#234b7c;
  --ink:#1c1c1c;
  --text:#444;
  --muted:#6b6b6b;
  --light:#f2f2f2;
  --line:#d8d8d8;
  --footer:#2d2d2d;
  --white:#fff;
}
*{box-sizing:border-box;margin:0;padding:0}
html,body{width:1200px;height:4249px;overflow:hidden}
body{font-family:'Montserrat',sans-serif;color:var(--ink);background:var(--white);position:relative}
.abs{position:absolute}
a{color:inherit}

/* header */
.site-header{position:absolute;left:0;top:0;width:1200px;height:110px;background:var(--white)}
.nav{position:absolute;left:96px;top:56px;display:flex;gap:35px;font-size:14px;color:#555}
.nav .active{color:var(--blue);font-weight:600}
.brand{position:absolute;left:520px;top:44px;width:160px;text-align:center;font-size:20px;font-weight:700;color:var(--ink);line-height:1.1}
.header-contact{position:absolute;top:46px;display:flex;align-items:center;gap:10px;font-size:15px;color:#333}
.icon-round{width:28px;height:28px;border-radius:50%;background:var(--blue);display:flex;align-items:center;justify-content:center}

/* hero */
.hero{position:absolute;left:0;top:110px;width:1200px;height:601px;background:linear-gradient(160deg,#dfe2e6 0%,#b9bcc2 35%,#8a3b3f 70%,#5a1a1f 100%)}
.hero-shade{position:absolute;inset:0;background:rgba(0,0,0,.22)}
.hero-title{position:absolute;left:0;width:1200px;top:225px;text-align:center;color:var(--white);font-size:38px;font-weight:800;letter-spacing:1px}
.hero-text{position:absolute;left:215px;width:770px;top:282px;text-align:center;color:var(--white);font-size:14px;line-height:25px}
.btn{display:inline-block;background:var(--blue);color:var(--white);font-weight:700;border-radius:6px;text-align:center}
.hero .btn{position:absolute;left:550px;top:366px;width:130px;height:32px;line-height:32px;font-size:13px}
.hero-arrow{position:absolute;top:268px;width:14px;height:14px;border-radius:50%;border:2px solid var(--white)}

/* welcome */
.welcome-brand{position:absolute;left:100px;top:880px;width:480px;text-align:center;font-size:76px;font-weight:800;color:var(--ink);line-height:1.05}
.welcome-title{position:absolute;left:638px;top:820px;font-size:29px;font-weight:700;line-height:40px}
.welcome-title span{color:var(--blue)}
.welcome-text{position:absolute;left:641px;top:906px;width:492px;font-size:16px;line-height:27px;color:var(--text)}
.welcome .btn{position:absolute;left:641px;top:1060px;width:107px;height:37px;line-height:37px;font-size:14px}

/* services */
.services{position:absolute;left:0;top:1215px;width:1200px;height:530px;background:var(--light)}
.section-title{position:absolute;left:0;width:1200px;text-align:center;font-size:31px;font-weight:700;letter-spacing:.5px}
.section-title span{color:var(--blue)}
.service{position:absolute;top:0;height:530px;width:600px}
.service.left{left:0;clip-path:polygon(0 0,100% 80px,100% 440px,0 525px);background:linear-gradient(120deg,#9fb3cc,#45607f 60%,#283d58)}
.service.right{left:600px;clip-path:polygon(0 80px,100% 0,100% 525px,0 440px);background:linear-gradient(120deg,#6e7480,#3b4049 55%,#23272e)}
.service-tint{position:absolute;inset:0;background:rgba(20,40,70,.35)}
.service h3{position:absolute;top:345px;color:var(--white);font-size:23px;font-weight:600}
.service p{position:absolute;top:385px;color:var(--white);font-size:14px}
.service a{position:absolute;top:414px;color:var(--white);font-size:13px;font-weight:700;text-decoration:underline}

/* products */
.products-title{top:1820px}
.card{position:absolute;width:240px;height:340px;background:var(--white);box-shadow:0 0 9px rgba(0,0,0,.14)}
.card .media{position:absolute;left:6px;top:6px;width:228px;height:176px;background:radial-gradient(circle at 50% 55%,#f6f6f6 0%,#dcdcdc 80%)}
.card h4{position:absolute;left:0;width:240px;top:206px;text-align:center;font-size:15px;font-weight:700}
.card p{position:absolute;left:18px;width:204px;top:234px;text-align:center;font-size:11.5px;line-height:18px;color:var(--muted)}
.doc-row{position:absolute;left:20px;top:279px;display:flex;gap:12px}
.doc{display:flex;height:36px;border:1px solid #b9c6d6;border-radius:5px;overflow:hidden;font-size:13px;font-weight:700;color:var(--blue)}
.doc span{display:flex;align-items:center;justify-content:center}
.doc .label{padding:0 10px}
.doc .dl{width:28px;background:var(--blue)}
.products .btn{position:absolute;left:547px;top:2628px;width:106px;height:36px;line-height:36px;font-size:14px}

/* distribution */
.map-area{position:absolute;left:0;top:2740px;width:718px;height:530px;background:#ececec}
.map-fill{position:absolute;left:125px;top:40px;width:385px;height:440px;background:linear-gradient(90deg,#b7b7b7 0%,#b7b7b7 25%,#2450a8 35%,#1c44a0 100%);border-radius:46% 40% 44% 38%}
.dist-panel{position:absolute;left:624px;top:2836px;width:576px;height:434px;background:var(--blue);color:var(--white)}
.dist-panel h2{position:absolute;left:80px;top:126px;font-size:29px;font-weight:700}
.dist-panel p{position:absolute;left:78px;top:178px;width:440px;font-size:17px;line-height:30px}

/* contact */
.contact{position:absolute;left:0;top:3270px;width:1200px;height:610px;background:linear-gradient(180deg,#f7f7f7,#eeeeee)}
.contact-title{top:140px}
.contact h3{position:absolute;left:145px;top:213px;font-size:21px;line-height:31px;font-weight:700}
.info-row{position:absolute;left:145px;display:flex;gap:14px;font-size:16px;line-height:28px;color:#333}
.info-row .icon-round{width:34px;height:34px;flex:none}
.field{position:absolute;height:48px;border:1.5px solid #333;border-radius:4px;background:var(--white);display:flex;align-items:center;gap:10px;padding-left:16px;font-size:12px;color:#333}
.field.area{height:142px;align-items:flex-start;padding-top:14px}
.contact .btn{position:absolute;left:534px;top:3765px;width:104px;height:34px;line-height:34px;font-size:13px}

/* footer */
.site-footer{position:absolute;left:0;top:3880px;width:1200px;height:369px;background:var(--footer);color:var(--white)}
.footer-brand{position:absolute;left:103px;top:80px;width:230px;font-size:36px;font-weight:700;line-height:1.15}
.social{position:absolute;top:232px;width:28px;height:28px;border-radius:50%;border:2px solid var(--white)}
.social.filled{background:var(--blue);border-color:var(--blue)}
.site-footer h5{position:absolute;top:62px;font-size:19px;font-weight:700}
.links{position:absolute;left:445px;top:100px;font-size:13.5px;line-height:25px;color:#ddd}
.links b{color:var(--white)}
.f-contact{position:absolute;left:630px;top:100px;width:250px;font-size:13.5px;line-height:24px}
.news{position:absolute;left:896px;top:98px;display:flex}
.news .input{width:200px;height:36px;border:1px solid #bbb;font-size:13px;line-height:34px;padding-left:12px;color:#ddd}
.news .go{width:36px;height:36px;background:var(--blue);display:flex;align-items:center;justify-content:center}
.footer-rule{position:absolute;left:94px;top:298px;width:1012px;height:1px;background:#555}
.copyright{position:absolute;left:0;width:1200px;top:326px;text-align:center;font-size:12.5px;color:#ddd}
</style>
</head>
<body>

<header class="site-header">
  <nav class="nav"><span class="active">Home</span><span>About us</span><span>Products</span><span>Distribution</span></nav>
  <div class="brand">FernMill Coatings</div>
  <div class="header-contact" style="left:727px">
    <span class="icon-round"><svg width="13" height="13" viewBox="0 0 24 24"><path fill="#fff" d="M6.6 10.8a15 15 0 006.6 6.6l2.2-2.2c.3-.3.7-.4 1-.2 1.1.4 2.3.6 3.6.6.6 0 1 .4 1 1V20c0 .6-.4 1-1 1A17 17 0 013 4c0-.6.4-1 1-1h3.5c.6 0 1 .4 1 1 0 1.3.2 2.5.6 3.6.1.3 0 .7-.2 1z"/></svg></span>01632 960418
  </div>
  <div class="header-contact" style="left:886px;font-size:13px">
    <span class="icon-round"><svg width="13" height="13" viewBox="0 0 24 24"><rect x="3" y="5" width="18" height="14" rx="2" fill="none" stroke="#fff" stroke-width="2"/><path d="M3 7l9 6 9-6" fill="none" stroke="#fff" stroke-width="2"/></svg></span>info@fernmillcoatings.co.uk
  </div>
</header>

<section class="hero" role="img" aria-label="Technician in protective suit spray painting a red car panel">
  <div class="hero-shade"></div>
  <span class="hero-arrow" style="left:38px"></span>
  <span class="hero-arrow" style="left:1144px"></span>
  <h1 class="hero-title">AUTOMOTIVE COATINGS</h1>
  <p class="hero-text">At FernMill Coatings we develop high performance automotive and industrial coatings that provide durable and high-quality finishes. Our next generation technologies offer ease of application, fast shop throughput and long-lasting performance.</p>
  <span class="btn">GET STARTED</span>
</section>

<section class="welcome">
  <div class="welcome-brand">FernMill Coatings</div>
  <h2 class="welcome-title">WELCOME TO<br><span>FERNMILL COATINGS</span></h2>
  <p class="welcome-text">At FernMill Coatings we develop high performance automotive and industrial coatings that provide durable and high-quality finishes. Our next generation technologies offer ease of application, fast shop throughput and long-lasting performance.</p>
  <span class="btn">Read More</span>
</section>

<section class="services">
  <div class="service left" role="img" aria-label="Painter in protective suit spraying a car">
    <div class="service-tint"></div>
    <h3 style="left:118px">Automotive Coating</h3>
    <p style="left:118px">Learn more about out automotive products</p>
    <a style="left:120px">Learn more</a>
  </div>
  <div class="service right" role="img" aria-label="Worker spray coating industrial pipework">
    <div class="service-tint"></div>
    <h3 style="left:91px">Industrial Coatings</h3>
    <p style="left:92px">Learn more about out industrial products</p>
    <a style="left:93px">Learn more</a>
  </div>
  <h2 class="section-title" style="top:36px">OUR <span>SERVICES</span></h2>
</section>

<section class="products">
  <h2 class="section-title products-title">OUR <span>PRODUCTS</span></h2>

  <div class="card" style="left:92px;top:1893px"><div class="media" role="img" aria-label="Aerosol can of acrylic primer"></div><h4>1K ACRYLIC PRIMER</h4><p>Lorem ipsum dolor sit amet, consectetur adipiscing elit aliqua.</p><div class="doc-row"><span class="doc"><span class="label">TDS</span><span class="dl"><svg width="14" height="14" viewBox="0 0 24 24"><path d="M12 3v12m-5-5l5 5 5-5M4 20h16" stroke="#fff" stroke-width="2.5" fill="none"/></svg></span></span><span class="doc"><span class="label">MSDS</span><span class="dl"><svg width="14" height="14" viewBox="0 0 24 24"><path d="M12 3v12m-5-5l5 5 5-5M4 20h16" stroke="#fff" stroke-width="2.5" fill="none"/></svg></span></span></div></div>
  <div class="card" style="left:351px;top:1893px"><div class="media" role="img" aria-label="Aerosol can of high gloss clear"></div><h4>1K HIGH GLOSS CLEAR</h4><p>Lorem ipsum dolor sit amet, consectetur adipiscing elit aliqua.</p><div class="doc-row"><span class="doc"><span class="label">TDS</span><span class="dl"><svg width="14" height="14" viewBox="0 0 24 24"><path d="M12 3v12m-5-5l5 5 5-5M4 20h16" stroke="#fff" stroke-width="2.5" fill="none"/></svg></span></span><span class="doc"><span class="label">MSDS</span><span class="dl"><svg width="14" height="14" viewBox="0 0 24 24"><path d="M12 3v12m-5-5l5 5 5-5M4 20h16" stroke="#fff" stroke-width="2.5" fill="none"/></svg></span></span></div></div>
  <div class="card" style="left:610px;top:1893px"><div class="media" role="img" aria-label="Aerosol can of satin clear"></div><h4>1K SATIN CLEAR</h4><p>Lorem ipsum dolor sit amet, consectetur adipiscing elit aliqua.</p><div class="doc-row"><span class="doc"><span class="label">TDS</span><span class="dl"><svg width="14" height="14" viewBox="0 0 24 24"><path d="M12 3v12m-5-5l5 5 5-5M4 20h16" stroke="#fff" stroke-width="2.5" fill="none"/></svg></span></span><span class="doc"><span class="label">MSDS</span><span class="dl"><svg width="14" height="14" viewBox="0 0 24 24"><path d="M12 3v12m-5-5l5 5 5-5M4 20h16" stroke="#fff" stroke-width="2.5" fill="none"/></svg></span></span></div></div>
  <div class="card" style="left:869px;top:1893px"><div class="media" role="img" aria-label="Aerosol can of matt clear"></div><h4>1K MATT CLEAR</h4><p>Lorem ipsum dolor sit amet, consectetur adipiscing elit aliqua.</p><div class="doc-row"><span class="doc"><span class="label">TDS</span><span class="dl"><svg width="14" height="14" viewBox="0 0 24 24"><path d="M12 3v12m-5-5l5 5 5-5M4 20h16" stroke="#fff" stroke-width="2.5" fill="none"/></svg></span></span><span class="doc"><span class="label">MSDS</span><span class="dl"><svg width="14" height="14" viewBox="0 0 24 24"><path d="M12 3v12m-5-5l5 5 5-5M4 20h16" stroke="#fff" stroke-width="2.5" fill="none"/></svg></span></span></div></div>

  <div class="card" style="left:92px;top:2253px"><div class="media" role="img" aria-label="Paint tin of PU primer"></div><h4>2K PU PRIMER</h4><p>Lorem ipsum dolor sit amet, consectetur adipiscing elit aliqua.</p><div class="doc-row"><span class="doc"><span class="label">TDS</span><span class="dl"><svg width="14" height="14" viewBox="0 0 24 24"><path d="M12 3v12m-5-5l5 5 5-5M4 20h16" stroke="#fff" stroke-width="2.5" fill="none"/></svg></span></span><span class="doc"><span class="label">MSDS</span><span class="dl"><svg width="14" height="14" viewBox="0 0 24 24"><path d="M12 3v12m-5-5l5 5 5-5M4 20h16" stroke="#fff" stroke-width="2.5" fill="none"/></svg></span></span></div></div>
  <div class="card" style="left:351px;top:2253px"><div class="media" role="img" aria-label="Paint tin of high gloss clear"></div><h4>2K HIGH GLOSS CLEAR</h4><p>Lorem ipsum dolor sit amet, consectetur adipiscing elit aliqua.</p><div class="doc-row"><span class="doc"><span class="label">TDS</span><span class="dl"><svg width="14" height="14" viewBox="0 0 24 24"><path d="M12 3v12m-5-5l5 5 5-5M4 20h16" stroke="#fff" stroke-width="2.5" fill="none"/></svg></span></span><span class="doc"><span class="label">MSDS</span><span class="dl"><svg width="14" height="14" viewBox="0 0 24 24"><path d="M12 3v12m-5-5l5 5 5-5M4 20h16" stroke="#fff" stroke-width="2.5" fill="none"/></svg></span></span></div></div>
  <div class="card" style="left:610px;top:2253px"><div class="media" role="img" aria-label="Paint tin of epoxy primer"></div><h4>2K EPOXY PRIMER</h4><p>Lorem ipsum dolor sit amet, consectetur adipiscing elit aliqua.</p><div class="doc-row"><span class="doc"><span class="label">TDS</span><span class="dl"><svg width="14" height="14" viewBox="0 0 24 24"><path d="M12 3v12m-5-5l5 5 5-5M4 20h16" stroke="#fff" stroke-width="2.5" fill="none"/></svg></span></span><span class="doc"><span class="label">MSDS</span><span class="dl"><svg width="14" height="14" viewBox="0 0 24 24"><path d="M12 3v12m-5-5l5 5 5-5M4 20h16" stroke="#fff" stroke-width="2.5" fill="none"/></svg></span></span></div></div>
  <div class="card" style="left:869px;top:2253px"><div class="media" role="img" aria-label="Paint tin of siloxane primer"></div><h4>1K SILOXANE PRIMER</h4><p>Lorem ipsum dolor sit amet, consectetur adipiscing elit aliqua.</p><div class="doc-row"><span class="doc"><span class="label">TDS</span><span class="dl"><svg width="14" height="14" viewBox="0 0 24 24"><path d="M12 3v12m-5-5l5 5 5-5M4 20h16" stroke="#fff" stroke-width="2.5" fill="none"/></svg></span></span><span class="doc"><span class="label">MSDS</span><span class="dl"><svg width="14" height="14" viewBox="0 0 24 24"><path d="M12 3v12m-5-5l5 5 5-5M4 20h16" stroke="#fff" stroke-width="2.5" fill="none"/></svg></span></span></div></div>

  <span class="btn">View More</span>
</section>

<section class="distribution">
  <div class="map-area"><div class="map-fill" role="img" aria-label="Map of the UK and Ireland with Great Britain highlighted in blue"></div></div>
  <div class="dist-panel">
    <h2>DISTRIBUTION</h2>
    <p>If you are interested in becoming a distributor for FernMill Coatings, please contact <a>info@fernmillcoatings.co.uk</a> for further information.</p>
  </div>
</section>

<section class="contact">
  <h2 class="section-title contact-title">CONTACT US</h2>
  <h3>Let's Make  Something<br>Great Together</h3>
  <div class="info-row" style="top:296px"><span class="icon-round"><svg width="14" height="14" viewBox="0 0 24 24"><path fill="#fff" d="M12 2a7 7 0 00-7 7c0 5 7 13 7 13s7-8 7-13a7 7 0 00-7-7zm0 9.5A2.5 2.5 0 1112 6.5a2.5 2.5 0 010 5z"/></svg></span><span>FernMill Coatings Ltd<br>Unit 4-5 Alder Way Business<br>Park Alder Way Hollinford, Wexby<br>WX9 2ZQ</span></div>
  <div class="info-row" style="top:418px;align-items:center"><span class="icon-round"><svg width="14" height="14" viewBox="0 0 24 24"><path fill="#fff" d="M6.6 10.8a15 15 0 006.6 6.6l2.2-2.2c.3-.3.7-.4 1-.2 1.1.4 2.3.6 3.6.6.6 0 1 .4 1 1V20c0 .6-.4 1-1 1A17 17 0 013 4c0-.6.4-1 1-1h3.5c.6 0 1 .4 1 1 0 1.3.2 2.5.6 3.6.1.3 0 .7-.2 1z"/></svg></span>01632 960418</div>
  <div class="info-row" style="top:476px;align-items:center"><span class="icon-round"><svg width="14" height="14" viewBox="0 0 24 24"><rect x="3" y="5" width="18" height="14" rx="2" fill="none" stroke="#fff" stroke-width="2"/><path d="M3 7l9 6 9-6" fill="none" stroke="#fff" stroke-width="2"/></svg></span>info@fernmillcoatings.co.uk</div>

  <div class="field" style="left:531px;top:201px;width:254px">&#9679; First Name</div>
  <div class="field" style="left:805px;top:201px;width:254px">&#9679; Last Name</div>
  <div class="field" style="left:531px;top:269px;width:254px">&#9993; Email</div>
  <div class="field" style="left:805px;top:269px;width:254px">&#9742; Phone</div>
  <div class="field area" style="left:531px;top:340px;width:528px">&#9993; Message</div>
</section>
<span class="btn" style="position:absolute;left:534px;top:3765px;width:104px;height:34px;line-height:34px;font-size:13px">SUBMIT</span>

<footer class="site-footer">
  <div class="footer-brand">FernMill Coatings</div>
  <span class="social filled" style="left:106px"></span>
  <span class="social" style="left:146px"></span>
  <h5 style="left:445px">Quick Links</h5>
  <div class="links"><b>Home</b><br>About us<br>Products<br>Distribution<br>Contact us</div>
  <h5 style="left:630px">Contact Us</h5>
  <div class="f-contact">FernMill Coatings Ltd<br>Unit 4-5 Alder Way Business Park Alder Way Hollinford, Wexby WX9 2ZQ<br><span style="display:block;margin-top:8px">&#9742; 01632 960418</span><span style="display:block;margin-top:12px">&#9993; info@fernmillcoatings.co.uk</span></div>
  <h5 style="left:896px">Newsletter</h5>
  <div class="news"><span class="input">Enter Email</span><span class="go"><svg width="14" height="14" viewBox="0 0 24 24"><path fill="#fff" d="M2 12l20-9-7 19-3-8z"/></svg></span></div>
  <div class="footer-rule"></div>
  <p class="copyright">© 2023 FernMill Coatings | All Rights Reserved</p>
</footer>

</body>
</html>
```